Web design for facial expression recognition service

We offer a service which allows customers to film large panels of participants looking at some video/screen (e.g. an advertisement) and to analyze the facial expressions shown by the participants. We are looking for the design of a new website which will make it easy for our customers to setup and view the results of these experiments online.
Competitor's websites that may serve as a reference are:
http://www.moravelt.example/pindor/#pane_overview
http://www.quintabrook.example/homepage.aspx
https://www.tavorlin.example/
The website will (for as far as the design is concerned) consist of three parts:
- A public home page (and perhaps some contact/news/about page), designed to catch the attention/interest potential customers.
- A (protected) project result page, showing the results in an interactive page with charts and numerical data.
- Pages (also protected) with fields and tables (setting up the project details).
The winner of this design project should provide us with at least one design for each of the above in order to get a complete 'theme' going which our developers can use. However, you are welcome to initially only provide the design for the project result page and/or home page.
We are looking for a modern, fresh, yet professional look (my client is a more established party in the field).
The final delivery should consist of layered Photoshop or Illustrator files.
Thank you in advance for participating!
Dear designers,
Reason: Extending the deadline by a few days to give designers a chance to submit designs for the other pages and process further feedback.
Target Market(s)
marketing research agencies (B2B service)
Industry/Entity Type
Delivery
Requirements
Must have
- Home page:
- Basic advertisement of the service; some quick explanation of how it works
- A way to login for existing users
- A link/button/banner inviting people to sign up
- Navigation controls to 2-3 other pages
- Social media links (Chatterbay, WorkNest group)
- Company logo (sorry, can't provide it as my client wishes to remain anonymous for now, but it's rounded and has blue as it's main color).
- Copyright / creator details
Project result page:
(see attachment 1 for a functional mockup - the design may follow this layout closely, or be completely different)
- Title
- A video player and basic numerical data
- Different views of the analysis results can dynamically be added/removed/collapsed/expanded; each one of these views will show some kind of chart, filters (combos), numerical data and a download button/link.
- A way to sign out, go to the main project page and go to the main page
- Logo
- Copyright
The form pages:
(see attachment 2 for a functional mockup of one of the pages; feel free to change some elements to better show the overall style)
- Title
- Text fields, combos, calendar pickers, tables, navigation links
- Logo
- Copyright
Nice to have
- Any creative text elements or product logo/symbol are a bonus. However, the basic "Lorem Ipsum" would do too.

```html
<!DOCTYPE html>
<html lang="en">
<head>
<meta charset="utf-8">
<title>Gazemetric — Rapid User Testing</title>
<link rel="stylesheet" href="https://fonts.googleapis.com/css2?family=Roboto+Slab:wght@300;400&family=Source+Sans+3:wght@400;600&family=Arimo:ital,wght@0,400;1,400&display=swap">
<style>
:root{
  --blue:#1a6fe0;
  --blue-deep:#1562cc;
  --accent-blue:#2a86f0;
  --green:#7cc33b;
  --green-dark:#5fa322;
  --grey-icon:#7b7b7b;
  --page:#eeeeee;
  --text:#333333;
  --muted:#8a8a8a;
  --logo-grey:#b4b4b4;
  --footer:#2c2c2c;
  --footer-link:#5f95d8;
  --white:#ffffff;
}
*{margin:0;padding:0;box-sizing:border-box}
html,body{width:980px;height:1200px;overflow:hidden}
body{background:var(--page);font-family:"Arimo",Arial,sans-serif;color:var(--text);position:relative}
.abs{position:absolute}

/* hero */
.hero{position:absolute;left:0;top:0;width:980px;height:366px;background:linear-gradient(180deg,var(--blue) 0%,var(--blue-deep) 100%)}
.brand{left:76px;top:20px;font-family:"Source Sans 3",sans-serif;font-weight:600;font-size:26px;color:var(--white);letter-spacing:-.3px}
.main-nav{left:0;top:28px;width:980px;font-family:"Source Sans 3",sans-serif;font-weight:600;font-size:13px;color:var(--white)}
.main-nav a{position:absolute;color:var(--white);text-decoration:none;white-space:nowrap}
.caret{display:inline-block;width:0;height:0;border-left:3px solid transparent;border-right:3px solid transparent;border-top:4px solid currentColor;margin-left:5px;vertical-align:middle}
.sign-in{left:806px;top:27px;font-family:"Source Sans 3",sans-serif;font-size:13px;color:#b9d4fa;display:flex;align-items:center;gap:8px}
.hero-title{left:75px;top:108px;font-family:"Roboto Slab",serif;font-weight:300;font-size:31px;color:var(--white)}
.hero-lead{left:77px;top:166px;width:270px;font-family:"Source Sans 3",sans-serif;font-size:15px;line-height:17.5px;color:var(--white)}
.cta{left:71px;top:280px;width:230px;height:37px;border-radius:19px;background:linear-gradient(180deg,#9bdb55 0%,var(--green) 55%,var(--green-dark) 100%);box-shadow:0 14px 14px -8px rgba(0,0,0,.35);font-family:"Source Sans 3",sans-serif;font-weight:600;font-size:15px;color:#3f7d12;text-align:center;line-height:37px}
.screen{border-radius:4px 4px 0 0;overflow:hidden;box-shadow:0 0 10px rgba(0,0,0,.3)}
.screen-back{left:372px;top:202px;width:130px;height:230px;background:linear-gradient(180deg,#e4e4e4 0%,#d6d6d6 30%,#eeeeee 100%)}
.screen-front{left:462px;top:158px;width:426px;height:274px;background:linear-gradient(180deg,#e6e6e6 0%,#e6e6e6 10%,#2b7ae8 12%,#2b7ae8 19%,#2a2a2a 20%,#2a2a2a 24%,#f4f4f4 26%,#ececec 100%)}
.screen-fade{left:360px;top:392px;width:540px;height:44px;background:linear-gradient(180deg,rgba(238,238,238,0) 0%,var(--page) 100%)}

/* how it works */
.section-rule{top:509px;height:1px;background:#d4d4d4}
.section-label{left:0;width:980px;top:502px;text-align:center;font-size:10px;letter-spacing:3px;color:#555}
.step-icon{width:68px;height:68px;border-radius:50%}
.step-title{font-family:"Roboto Slab",serif;font-weight:300;font-size:18px;line-height:24px;color:var(--text)}
.step-title .step-num{color:var(--accent-blue);display:block}
.step-text{width:256px;font-size:11px;line-height:17px;color:#444}
.read-more{left:734px;top:730px;display:flex;align-items:center;gap:10px;font-size:11px;color:var(--accent-blue)}
.read-more span{text-decoration:underline}
.divider{left:0;top:786px;width:980px;height:12px;background:linear-gradient(180deg,rgba(0,0,0,.06),rgba(0,0,0,0))}

/* testimonials */
.avatar{width:56px;height:56px;border-radius:50%;border:2px solid var(--white);box-shadow:0 1px 3px rgba(0,0,0,.2)}
.quote{left:212px;width:360px;font-style:italic;font-size:11px;line-height:18px;color:#444}
.quote cite{display:block;font-style:normal;color:var(--muted)}
.client{font-family:"Source Sans 3",sans-serif;font-weight:600;font-size:13px;color:var(--logo-grey);letter-spacing:2px;text-align:center;width:100px}

/* footer */
.footer-band{left:0;top:1080px;width:980px;height:6px;background:#d9d9d9}
.footer{left:0;top:1086px;width:980px;height:114px;background:var(--footer)}
.social{top:1141px;font-family:"Source Sans 3",sans-serif;font-size:11px;color:#6e6e6e}
.footer-brand{left:787px;top:1130px;font-family:"Source Sans 3",sans-serif;font-weight:600;font-size:24px;color:var(--white);letter-spacing:-.3px}
.footer-link{top:1173px;font-size:11px;color:var(--footer-link);text-decoration:none}
.copyright{left:810px;top:1173px;font-size:11px;color:#555}
</style>
</head>
<body>

<header class="hero">
  <div class="abs brand">gazemetric</div>
  <nav class="abs main-nav">
    <a style="left:240px" href="#">How it Works<span class="caret"></span></a>
    <a style="left:355px" href="#">Submit your Project</a>
    <a style="left:491px" href="#">Term &amp; Pricing</a>
    <a style="left:599px" href="#">About Us</a>
    <a style="left:680px" href="#">Contact</a>
  </nav>
  <div class="abs sign-in">
    <svg width="14" height="16" viewBox="0 0 14 16" aria-hidden="true"><circle cx="7" cy="4.5" r="3.5" fill="#b9d4fa"/><path d="M0 16c0-4.5 3-7 7-7s7 2.5 7 7z" fill="#b9d4fa"/></svg>
    Sign in<span class="caret"></span>
  </div>
  <h1 class="abs hero-title">Rapid User Testing</h1>
  <p class="abs hero-lead">Learn why users leave. Start a study and get videos of real people using your site. Results as fast as an hour.</p>
  <a class="abs cta" href="#">SING UP GAZEMETRIC NOW!</a>
</header>

<div class="abs screen screen-back" role="img" aria-label="Browser window showing the project information form page"></div>
<div class="abs screen screen-front" role="img" aria-label="Browser window showing the project result page with a line graph and video panel"></div>
<div class="abs screen-fade"></div>

<section>
  <div class="abs section-rule" style="left:58px;width:360px"></div>
  <div class="abs section-rule" style="left:590px;width:298px"></div>
  <h2 class="abs section-label">HOW DOES IT WORK?</h2>

  <svg class="abs step-icon" style="left:66px;top:560px" viewBox="0 0 68 68" aria-hidden="true">
    <circle cx="34" cy="34" r="34" fill="var(--accent-blue)"/>
    <circle cx="34" cy="27" r="8" fill="#fff"/>
    <path d="M20 48c0-9 6-13 14-13s14 4 14 13z" fill="#fff"/>
  </svg>
  <div class="abs step-title" style="left:146px;top:573px"><span class="step-num">Step 1:</span>Create an account</div>
  <p class="abs step-text" style="left:59px;top:660px">Lorem ipsum dolor sit amet, consec tetuer adipicing it. Praesent vestibulum molestie lacusnen ummyhe. Odre-rit mauris.</p>

  <svg class="abs step-icon" style="left:369px;top:560px" viewBox="0 0 68 68" aria-hidden="true">
    <circle cx="34" cy="34" r="34" fill="var(--green)"/>
    <rect x="20" y="20" width="26" height="28" rx="3" fill="none" stroke="#fff" stroke-width="3"/>
    <path d="M30 40l2-7 14-14 5 5-14 14z" fill="#fff" stroke="var(--green)" stroke-width="1.5"/>
  </svg>
  <div class="abs step-title" style="left:449px;top:573px"><span class="step-num">Step 2:</span>Fill the form</div>
  <p class="abs step-text" style="left:358px;top:660px">Lorem ipsum dolor sit amet, consec tetuer adipicing it. Praesent vestibulum molestie lacusnen ummyhe. Odre-rit mauris.</p>

  <svg class="abs step-icon" style="left:668px;top:560px" viewBox="0 0 68 68" aria-hidden="true">
    <circle cx="34" cy="34" r="34" fill="var(--grey-icon)"/>
    <rect x="20" y="20" width="28" height="28" rx="3" fill="none" stroke="#fff" stroke-width="3"/>
    <path d="M24 42l7-9 5 5 8-12" fill="none" stroke="#fff" stroke-width="3" stroke-linejoin="round"/>
  </svg>
  <div class="abs step-title" style="left:748px;top:573px"><span class="step-num">Step 3:</span>Analyze &amp; Result</div>
  <p class="abs step-text" style="left:658px;top:660px">Lorem ipsum dolor sit amet, consec tetuer adipicing it. Praesent vestibulum molestie lacusnen ummyhe. Odre-rit mauris.</p>

  <a class="abs read-more" href="#">
    <svg width="14" height="14" viewBox="0 0 14 14" aria-hidden="true"><circle cx="7" cy="7" r="7" fill="#bdbdbd"/><path d="M6 4l3 3-3 3" fill="none" stroke="#fff" stroke-width="1.6"/></svg>
    <span>Read More about our products</span>
  </a>
</section>

<div class="abs divider"></div>

<section>
  <div class="abs avatar" style="left:120px;top:858px;background:linear-gradient(135deg,#5a4036,#d8b49a)" role="img" aria-label="Portrait photo of a customer"></div>
  <blockquote class="abs quote" style="top:857px">“ Lorem ipsum dolor sit amet, consec tetuer adipicing it. Praesent vestibulum molestie lacusnen ummyhe. Odrerit mauris. Phasellus portacepicit”<cite>- Lorem Ipsum</cite></blockquote>

  <div class="abs avatar" style="left:120px;top:950px;background:linear-gradient(135deg,#6b4a30,#e2c0a4)" role="img" aria-label="Portrait photo of a customer"></div>
  <blockquote class="abs quote" style="top:949px">“ Lorem ipsum dolor sit amet, consec tetuer adipicing it. Praesent vestibulum molestie lacusnen ummyhe. Odrerit mauris. Phasellus portacepicit varius ”<cite>- Lorem Ipsum</cite></blockquote>

  <div class="abs client" style="left:594px;top:860px">ORVANE</div>
  <div class="abs client" style="left:690px;top:860px">KESTREL</div>
  <div class="abs client" style="left:778px;top:860px">ORVANE</div>
  <div class="abs client" style="left:594px;top:911px">LUMERA</div>
  <div class="abs client" style="left:690px;top:911px">BRISKO</div>
  <div class="abs client" style="left:778px;top:911px">LUMERA</div>
  <div class="abs client" style="left:594px;top:959px">ORVANE</div>
  <div class="abs client" style="left:690px;top:959px">KESTREL</div>
  <div class="abs client" style="left:778px;top:959px">ORVANE</div>
</section>

<div class="abs footer-band"></div>
<footer class="abs footer"></footer>
<a class="abs social" style="left:585px" href="#">Chatterbay</a>
<a class="abs social" style="left:646px" href="#">WorkNest</a>
<a class="abs social" style="left:700px" href="#">Plusring</a>
<div class="abs footer-brand">gazemetric</div>
<a class="abs footer-link" style="left:512px" href="#">Legal Notice</a>
<a class="abs footer-link" style="left:601px" href="#">Sitemap</a>
<a class="abs footer-link" style="left:671px" href="#">Contact Us</a>
<div class="abs copyright">© 2013 Gazemetric</div>

</body>
</html>
```